https://dorvakel.com

We need a cool technology design for our Managed IT Services company. We are located in Coral Springs Florida. We provide all IT services and support for small to medium sized businesses. We would like to see designs that use our blue and white colors from our website.

```html
<!DOCTYPE html>
<html lang="en">
<head>
<meta charset="UTF-8">
<title>Dorvakel Business Card</title>
<link rel="stylesheet" href="https://fonts.googleapis.com/css2?family=Montserrat:wght@600;700&family=Open+Sans:wght@400;600&display=swap">
<style>
  :root {
    --navy: #133159;
    --white: #ffffff;
    --grey-mark: #6f7176;
    --text-dark: #3a3d44;
    --divider: #d3d6db;
    --stage: #5e5e5e;
  }
  * { margin: 0; padding: 0; box-sizing: border-box; }
  html, body { width: 1200px; height: 1200px; overflow: hidden; }
  body {
    background: var(--stage);
    position: relative;
    font-family: "Open Sans", sans-serif;
  }
  .card {
    position: absolute;
    left: 180px;
    width: 840px;
    height: 480px;
    border-radius: 36px;
    overflow: hidden;
  }
  .card--back {
    top: 90px;
    background: var(--navy);
    display: flex;
    flex-direction: column;
    align-items: center;
    justify-content: center;
  }
  .back-wordmark {
    font-family: "Montserrat", sans-serif;
    font-weight: 600;
    font-size: 96px;
    letter-spacing: 1px;
    color: var(--white);
    line-height: 1;
  }
  .back-url {
    margin-top: 60px;
    font-size: 22px;
    font-weight: 600;
    letter-spacing: 1.5px;
    color: var(--white);
  }
  .card--front {
    top: 630px;
    background: var(--white);
  }
  .front-wordmark {
    position: absolute;
    left: 90px;
    top: 170px;
    width: 330px;
    font-family: "Montserrat", sans-serif;
    font-weight: 600;
    font-size: 52px;
    color: var(--grey-mark);
    line-height: 1;
    white-space: nowrap;
  }
  .front-divider {
    position: absolute;
    left: 450px;
    top: 60px;
    width: 2px;
    height: 210px;
    background: var(--divider);
  }
  .contact {
    position: absolute;
    left: 480px;
    top: 60px;
    width: 330px;
    color: var(--text-dark);
  }
  .contact__name {
    font-family: "Montserrat", sans-serif;
    font-weight: 700;
    font-size: 28px;
    color: var(--navy);
    line-height: 1.1;
  }
  .contact__role {
    font-size: 18px;
    margin-bottom: 22px;
  }
  .contact__line {
    display: flex;
    align-items: flex-start;
    gap: 10px;
    font-size: 18px;
    line-height: 1.35;
    margin-bottom: 6px;
  }
  .contact__line svg { flex: none; margin-top: 4px; }
  .front-band {
    position: absolute;
    left: 0;
    bottom: 16px;
    width: 100%;
    height: 72px;
    background: var(--navy);
    display: flex;
    align-items: center;
    padding-left: 60px;
  }
  .front-url {
    font-size: 22px;
    font-weight: 600;
    letter-spacing: 6px;
    color: var(--white);
  }
</style>
</head>
<body>
  <section class="card card--back">
    <div class="back-wordmark">DORVAKEL</div>
    <div class="back-url">www.dorvakel.com</div>
  </section>

  <section class="card card--front">
    <div class="front-wordmark">DORVAKEL</div>
    <div class="front-divider"></div>
    <div class="contact">
      <div class="contact__name">JOHN DOE</div>
      <div class="contact__role">Director</div>
      <div class="contact__line">
        <svg width="16" height="16" viewBox="0 0 24 24" aria-hidden="true">
          <path fill="#133159" d="M6.6 10.8a15 15 0 0 0 6.6 6.6l2.2-2.2a1 1 0 0 1 1-.25 11.4 11.4 0 0 0 3.6.57 1 1 0 0 1 1 1V20a1 1 0 0 1-1 1A17 17 0 0 1 3 4a1 1 0 0 1 1-1h3.5a1 1 0 0 1 1 1c0 1.25.2 2.450.57 3.57a1 1 0 0 1-.25 1z"/>
        </svg>
        <span>(954) 555-0142</span>
      </div>
      <div class="contact__line">
        <svg width="16" height="16" viewBox="0 0 24 24" aria-hidden="true">
          <path fill="#133159" d="M12 2a7 7 0 0 0-7 7c0 5.2 7 13 7 13s7-7.8 7-13a7 7 0 0 0-7-7zm0 9.5A2.5 2.5 0 1 1 12 6.5a2.5 2.5 0 0 1 0 5z"/>
        </svg>
        <span>2210 Palm Crest Ave #118<br>Coral Springs, Florida 33065</span>
      </div>
    </div>
    <div class="front-band">
      <span class="front-url">www.dorvakel.com</span>
    </div>
  </section>
</body>
</html>
```